Premium Personal Brand — Facebook Banner (Used Across All Platforms)

Update — Additional Color Direction
In addition to the dark charcoal/slate direction already described, I'm also interested in seeing variants with:
Dark navy blue — Deep, authoritative, intelligence-community feel. Same textured/matte treatment, not flat or bright.
Warm charcoal with steel blue accent — Keep the dark base but introduce a subtle steel blue gradient, accent line, or tonal shift. Sophisticated, modern, adds dimension without adding color noise.
Both should maintain the same premium, restrained, architectural feel described in the original brief. No bright blues, no corporate PowerPoint energy — think midnight, think depth, think weight.
Everything else in the brief remains the same.
I am building a premium personal brand as an executive advisor to founders ($5M+ revenue).
This contest is Facebook-banner–focused, but the design must represent a visual system that will be reused across:
- LinkedIn
- YouTube
I- nstagram
- X (Twitter)
- Website hero sections and other brand touchpoints
Think of the Facebook banner as the primary expression of the brand — not a one-off graphic.
This project is about discovering a high-end visual style and brand feel, not decoration.
What to design
Please submit one cohesive visual system, shown primarily as:
- Facebook banner (primary focus)
The same design language should clearly translate to all platforms listed above.
Designers are responsible for using the current recommended dimensions for each platform.
Quick clarification on background direction:
Backgrounds should have depth and texture, not flat color fields. Avoid pure white, light grey, or solid black backgrounds. Think matte, architectural materials — stone, graphite, concrete, steel — not blank canvases. Subtle tonal variation is encouraged. Obvious gradients or decorative patterns are not.
Text to use
Primary Headline:
- Your Business Is Too Valuable To Be Run On Hope.
Subheadline:
- You didn’t build a business to become its prisoner.
Name:
Paul Whitaker
The headline should be the dominant visual element.
Logo note (important)
My personal logo is currently being finalized.
For this contest:
- Use a simple “PW” monogram placeholder
- Clean, bold, geometric sans-serif
- Do not design a logo
- The winning design must allow an easy logo swap later.
Headshot note (important)
- Please do not include a headshot in the banner design.
- Most platforms display a circular profile image separately.
- The banner should stand on its own using typography, layout, and tone only.
- Design the banner assuming the profile photo will sit nearby, not inside the banner.
Style direction
The design should feel:
- Premium
- Calm
- Confident
- Restrained
- High-trust
- Dark, neutral backgrounds are preferred.
- Fewer elements are better than more.
Think:
- Owner-level advisor
- Private equity / boardroom tone
- Industrial, Modern, Minimalist, Elite, Architectural, not decorative
What to avoid
Please do not submit designs that feel:
- Promotional, hype-driven, or salesy
- Like a coach, guru, or agency
- Bright, colorful, or gradient-heavy
- Busy or over-designed
- Based on stock photos
- No motivational speaker energy.
Reaction test
- If someone sees this banner on Facebook (or later on LinkedIn, YouTube, etc.), the reaction should be:
“That person is serious. I’d trust them with important decisions.”
Final note
- I am not looking for many variations.
- I am looking for one strong visual direction you believe in.
Simple beats clever.
- Restraint beats decoration.

```html
<!DOCTYPE html>
<html lang="en">
<head>
<meta charset="utf-8">
<title>Paul Whitaker — Executive Advisor to Founders</title>
<link rel="stylesheet" href="https://fonts.googleapis.com/css2?family=Fira+Sans:wght@400;500&display=swap">
<style>
  :root {
    --navy-deep: #0a1a4e;
    --navy-mid: #143a8c;
    --navy-light: #2a63c4;
    --glow: #5fa8f0;
    --text-main: #eef1f8;
    --text-soft: #dfe5f2;
    --mark-bg: rgba(40, 58, 110, 0.75);
    --mark-border: rgba(150, 170, 215, 0.45);
  }
  * { margin: 0; padding: 0; box-sizing: border-box; }
  html, body { width: 1200px; height: 800px; overflow: hidden; }
  body { font-family: "Fira Sans", sans-serif; background: var(--navy-deep); }

  .banner {
    position: relative;
    width: 1200px;
    height: 800px;
    overflow: hidden;
    background:
      radial-gradient(ellipse 700px 520px at 1150px 40px, rgba(95,168,240,0.45), transparent 70%),
      radial-gradient(ellipse 900px 600px at 700px 450px, rgba(30,80,170,0.55), transparent 75%),
      linear-gradient(160deg, var(--navy-deep) 0%, var(--navy-mid) 55%, #0f2f78 100%);
  }
  .network-texture {
    position: absolute;
    right: 0;
    top: 150px;
    width: 420px;
    height: 420px;
    background: radial-gradient(circle at 60% 45%, rgba(95,168,240,0.22), transparent 70%);
  }

  .brand-row {
    position: absolute;
    left: 55px;
    top: 155px;
    display: flex;
    align-items: center;
    gap: 18px;
  }
  .monogram {
    width: 76px;
    height: 53px;
    display: flex;
    align-items: center;
    justify-content: center;
    background: var(--mark-bg);
    border: 1px solid var(--mark-border);
    color: var(--text-main);
    font-size: 32px;
    font-weight: 500;
  }
  .tagline {
    color: var(--text-soft);
    font-size: 28px;
    font-weight: 400;
    letter-spacing: 2.2px;
    text-transform: uppercase;
  }

  .headline {
    position: absolute;
    left: 55px;
    top: 242px;
    color: var(--text-main);
    font-size: 58px;
    font-weight: 500;
    line-height: 73px;
    letter-spacing: -0.3px;
    text-shadow: 0 2px 10px rgba(0,0,0,0.25);
  }
  .subheadline {
    position: absolute;
    left: 55px;
    top: 418px;
    color: var(--text-soft);
    font-size: 31px;
    font-weight: 400;
  }
  .signature {
    position: absolute;
    left: 57px;
    top: 550px;
  }
  .signature .name {
    color: var(--text-main);
    font-size: 38px;
    font-weight: 500;
  }
  .signature .role {
    margin-top: 20px;
    color: var(--text-soft);
    font-size: 26px;
    font-weight: 400;
  }
</style>
</head>
<body>
  <main class="banner">
    <div class="network-texture" role="img" aria-label="Soft constellation of connected points glowing in blue"></div>

    <div class="brand-row">
      <div class="monogram">PW</div>
      <p class="tagline">Driving Success Through</p>
    </div>

    <h1 class="headline">Your Business Is Too Valuable<br>To Be Run On Hope.</h1>
    <p class="subheadline">You didn't build a business to become its prisoner.</p>

    <div class="signature">
      <p class="name">Paul Whitaker</p>
      <p class="role">Executive Advisor to Founders ($5M+)</p>
    </div>
  </main>
</body>
</html>
```